DL Flyer for vehicle buying/selling service and advice business

New business to help people sell their current vehicle then select and buy and maintain their next car. (New or used).
We'll prepare and sell your car for you and get $,000s more than a trade in.
Offer advice as to the best car currently on the market based on our customer's needs.
With country wide sourcing network of cars across all manufacturers we have great buying power to ensure the very best possible price.
Personal service, including preparation of car for sale, pickup of old and drop-off of new vehicles, organise RWC and any required repairs.
We are NOT a car dealer so we WILL not try to sell you the vehicles we own.
Totally impartial, professional and friendly service making the purchase of your next car a great experience.
Updates

Flyer wording===========“Don’t sell your car or buy your next car without speaking to us”We guarantee to get you a better price for your current car and to find a cheaper purchase price for your next car.With a country wide sourcing network of cars “new and used” across all manufacturers we have sensational buying power to ensure the very best possible price.We can source the right car on any budget, from $2,000 to $200,000We are NOT a car dealer so we WILL not try to sell you the vehicles we own.By not being affiliated with any individual car manufacturer or dealer we can offer absolute impartiality.We’ll sit with you to discuss the best car for your needs and even bring the car to you for a test drive without the pressure of a salesperson nearby.Our services include:• Selling your current car: - Obtaining a roadworthy certificate - Organising any repairs needed - Detailing your car (wash, vacuum, polish) - Advertising of your car - Dealing with potential buyers - Negotiating the best price on your behalf• Assisting with the selection of your next car• Organising test drives• Purchasing the car of your choice - Sourcing the very best price• Ongoing management of their vehicle (service, clean, repair)Possible inclusions in the flyer might be:Advantages of upgrading to a new vehicle include:o reliability, o safety,o fuel efficiencyo comfort.Space for a couple of short testimonials Background images of all of the major car manufacturers Added Friday, July 29, 2016

Target Market(s)

Local community.
Initially will drop DL flyers in local post boxes

Industry/Entity Type

Business

Requirements
Must have
• Flyer wording:
• ===========
• “Don’t sell your car or buy your next car without speaking to us”
• ---------------------------------------------------------------------------------
• We guarantee to get you a better price for your current car and to find a cheaper purchase price for your next car.
• With a country wide sourcing network of cars “new and used” across all manufacturers we have sensational buying power to ensure the very best possible price.
• We can source the right car on any budget, from $2,000 to $200,000
• We are NOT a car dealer so we WILL not try to sell you the vehicles we own.
• By not being affiliated with any individual car manufacturer or dealer we can offer absolute impartiality.
• We’ll sit with you to discuss the best car for your needs and even bring the car to you for a test drive without the pressure of a salesperson nearby.
• Our services include:
• • Selling your current car:
• o Obtaining a roadworthy certificate
• o Organising any repairs needed
• o Detailing your car (wash, vacuum, polish)
• o Advertising of your car
• o Dealing with potential buyers
• o Negotiating the best price on your behalf
• • Assisting with the selection of your next car
• • Organising test drives
• • Purchasing the car of your choice
• o Sourcing the very best price
• • Ongoing management of your vehicle (service, clean, repair)
• Call Gerald on: 0427 315064
Nice to have
• Possible inclusions on the flyer might be:
• List of advantages of upgrading to a new vehicle:
• o reliability,
• o safety,
• o fuel efficiency
• o comfort
• Space for a couple of short testimonials
• Background images of all of the major car manufacturers

```html
<!DOCTYPE html>
<html lang="en">
<head>
<meta charset="utf-8">
<title>DriveWise Brokers – DL Flyer</title>
<link href="https://fonts.googleapis.com/css2?family=Arimo:wght@400;700&family=Roboto+Condensed:wght@700&family=Open+Sans:wght@400;600;700&family=Questrial&display=swap" rel="stylesheet">
<style>
  :root{
    --red:#e8212a;
    --charcoal:#3b3b3d;
    --ink:#333333;
    --rule:#d6d6d6;
    --paper:#ffffff;
    --backdrop:#d9d9d9;
  }
  *{margin:0;padding:0;box-sizing:border-box}
  html,body{width:1200px;height:1200px;overflow:hidden}
  body{background:var(--backdrop);position:relative;font-family:"Open Sans",sans-serif;color:var(--ink)}
  .flyer{position:absolute;top:58px;width:482px;height:1084px;background:var(--paper);overflow:hidden}
  .flyer--front{left:96px}
  .flyer--back{left:622px}
  .flyer__shapes{position:absolute;inset:0;width:100%;height:100%}

  .headline{position:absolute;left:0;right:0;top:26px;color:#fff;font-family:"Arimo",sans-serif;font-weight:400}
  .headline__main{position:absolute;left:28px;top:0;font-weight:700;font-size:41px;line-height:1;white-space:nowrap}
  .headline__sub{position:absolute;left:84px;top:40px;font-weight:400;font-size:38px;line-height:1;white-space:nowrap}
  .headline__tail{position:absolute;left:103px;top:82px;font-family:"Roboto Condensed",sans-serif;font-weight:700;font-size:31px;line-height:1;white-space:nowrap;letter-spacing:-.3px}

  .guarantee{position:absolute;left:35px;top:600px;width:410px;height:86px;border-radius:14px;
    background:linear-gradient(#5a5a5c,#3d3d3f);border:2px solid #fff;box-shadow:0 2px 4px rgba(0,0,0,.25);
    padding:10px 14px;font-family:"Questrial",sans-serif;font-size:17px;line-height:20px;color:#fff}
  .guarantee em{font-style:normal;color:var(--red)}

  .facts{position:absolute;top:703px;left:36px;right:30px;display:flex;font-size:13.4px;line-height:18.6px;color:var(--ink)}
  .facts__col{width:212px}
  .facts__divider{width:1px;height:108px;background:#444;margin:0 20px 0 0}
  .facts__col--budget{width:200px}
  .budget{display:block;color:var(--red);font-family:"Arimo",sans-serif;font-weight:700;font-size:17px;line-height:22px}
  .note{display:block;font-size:10.8px;line-height:15px;margin-top:8px}
  .body-copy{position:absolute;left:36px;right:40px;font-size:13.4px;line-height:18.6px}

  .contact{position:absolute;left:0;right:0;text-align:center;color:#fff}
  .contact__call{font-family:"Arimo",sans-serif;font-weight:700;font-size:29px;line-height:1;white-space:nowrap}
  .contact__web{font-family:"Arimo",sans-serif;font-weight:700;font-size:16px;letter-spacing:4px;margin-top:6px}

  .services__title{position:absolute;left:0;right:0;top:26px;text-align:center;color:#fff;font-family:"Arimo",sans-serif;font-weight:700;font-size:43px}
  .services{position:absolute;top:145px;left:0;right:0;list-style:none;text-align:center;font-weight:600;font-size:16.4px}
  .services li{height:33px;line-height:33px;position:relative;white-space:nowrap}
  .services li::after{content:"";position:absolute;left:110px;right:110px;bottom:0;height:1px;background:var(--rule)}
  .services li.wrap{height:auto;line-height:33px;white-space:normal;padding:0 44px}
  .services li:last-child::after{display:none}
</style>
</head>
<body>

<section class="flyer flyer--front">
  <svg class="flyer__shapes" viewBox="0 0 482 1084" preserveAspectRatio="none">
    <defs>
      <linearGradient id="showroomFront" x1="0" y1="0" x2="1" y2="1">
        <stop offset="0" stop-color="#e9ecef"/>
        <stop offset=".55" stop-color="#c9cdd2"/>
        <stop offset="1" stop-color="#9c3a3e"/>
      </linearGradient>
    </defs>
    <rect x="0" y="195" width="482" height="425" fill="url(#showroomFront)" role="img" aria-label="Photo of a family shaking hands with a car adviser in a showroom"/>
    <path d="M0 125 C150 182 330 194 482 190 L482 206 C300 212 150 210 0 200 Z" fill="var(--charcoal)"/>
    <path d="M0 118 C150 176 330 184 482 176 L482 190 C330 194 150 182 0 125 Z" fill="#fff"/>
    <path d="M0 0 H482 V176 C330 184 150 176 0 118 Z" fill="var(--red)"/>
    <path d="M0 988 Q241 938 482 975 V1084 H0 Z" fill="var(--red)"/>
  </svg>

  <h1 class="headline">
    <span class="headline__main">“DON’T sell your car</span>
    <span class="headline__sub">or buy your next car</span>
    <span class="headline__tail">WITHOUT SPEAKING TO US„</span>
  </h1>

  <p class="guarantee"><em>We guarantee</em> to get you a better price for your current car and to find a cheaper purchase price for your next car.</p>

  <div class="facts">
    <p class="facts__col">With a country wide sourcing network of cars “<b>new and used</b>” across all manufacturers we have sensational buying power to ensure the very best possible price.</p>
    <span class="facts__divider"></span>
    <p class="facts__col facts__col--budget">We can source the right car on any budget, from
      <span class="budget">$2,000 to $200,000</span>
      <span class="note">We are <b>NOT</b> a car dealer so we <b>WILL</b> not try to sell you the vehicles we own</span>
    </p>
  </div>

  <p class="body-copy" style="top:831px">By not being affiliated with any individual car manufacturer or dealer we can offer absolute impartiality.</p>
  <p class="body-copy" style="top:894px">We’ll sit with you to discuss the best car for your needs and even bring the car to you for a test drive without the pressure of a salesperson nearby</p>

  <div class="contact" style="top:1004px">
    <p class="contact__call">Call Gerald on: 0427 315064</p>
    <p class="contact__web">www.drivewisebrokers.com</p>
  </div>
</section>

<section class="flyer flyer--back">
  <svg class="flyer__shapes" viewBox="0 0 482 1084" preserveAspectRatio="none">
    <defs>
      <linearGradient id="showroomBack" x1="0" y1="0" x2="1" y2="1">
        <stop offset="0" stop-color="#3a3b40"/>
        <stop offset=".5" stop-color="#b9a48a"/>
        <stop offset="1" stop-color="#c9d3e2"/>
      </linearGradient>
    </defs>
    <rect x="0" y="520" width="482" height="564" fill="url(#showroomBack)" role="img" aria-label="Photo of a couple signing papers with a car adviser at a dealership desk"/>
    <path d="M0 500 C120 640 300 690 482 680 L482 700 C300 705 100 690 0 590 Z" fill="var(--charcoal)"/>
    <path d="M0 0 H482 V672 C300 682 120 640 0 520 Z" fill="#fff"/>
    <path d="M0 38 C120 110 330 118 482 102 L482 118 C320 132 120 125 0 118 Z" fill="var(--charcoal)"/>
    <path d="M0 0 H482 V100 C330 112 130 108 0 40 Z" fill="var(--red)"/>
    <path d="M0 1000 Q241 958 482 990 V1084 H0 Z" fill="var(--red)"/>
  </svg>

  <h2 class="services__title">Our services</h2>

  <ul class="services">
    <li>Selling your current car:</li>
    <li>Obtaining a roadworthy certificate</li>
    <li>Organising any repairs needed</li>
    <li>Detailing your car (wash, vacuum, polish)</li>
    <li>Advertising of your car</li>
    <li>Dealing with potential buyers</li>
    <li>Negotiating the best price on your behalf</li>
    <li>Assisting with the selection of your next car</li>
    <li>Organising test drives</li>
    <li>Purchasing the car of your choice</li>
    <li>Sourcing the very best price</li>
    <li class="wrap">Ongoing management of your vehicle (service, clean, repair)</li>
  </ul>

  <div class="contact" style="top:1016px">
    <p class="contact__call">Call Gerald on: 0427 315064</p>
    <p class="contact__web">www.drivewisebrokers.com</p>
  </div>
</section>

</body>
</html>
```